Larkin Ridge Provisions Co Website Creation

We need a website designed that goes along with our western/cattle brand vibe that our logo has. We are going to need a couple different pages including: About Us, Meat Boxes, Recipes, Contact Us.

We are going to need a shop so that people may visit the website and order meat boxes to be shipped or delivered at their home. Our mission is to provide the highest quality meat that every family can afford.

Would love to see the website design with lots of mountain range backgrounds and create a feel of open range beef that has a tradition of providing great beef. Family owned business that has been raising cattle for over 30 years.

Love the colors of using dark greens, browns, Tans, Blacks

```html
<!DOCTYPE html>
<html lang="en">
<head>
<meta charset="utf-8">
<title>Larkin Ridge Provisions Co</title>
<link href="https://fonts.googleapis.com/css2?family=Bebas+Neue&family=Montserrat:wght@400;500;600;700&display=swap" rel="stylesheet">
<style>
:root{
  --green:#0f3d22;
  --brown:#3d1a08;
  --tan:#d6b98a;
  --cream:#ece3d0;
  --card:#fbf8f2;
  --ink:#1b1b1b;
  --text:#3c3c3c;
  --bar:#2b2b2b;
  --footer:#2a2a2c;
}
*{margin:0;padding:0;box-sizing:border-box}
html,body{width:1200px;height:3854px;overflow:hidden}
body{position:relative;font-family:'Montserrat',sans-serif;color:var(--text);background:#fff}
.abs{position:absolute}
.display{font-family:'Bebas Neue',sans-serif;color:var(--ink);letter-spacing:.5px;line-height:1}
.btn{position:absolute;display:flex;align-items:center;justify-content:center;border-radius:30px;font-weight:700;font-size:14px;text-transform:uppercase}

.topbar{left:0;top:0;width:1200px;height:45px;background:var(--bar);color:#fff;font-size:13px;display:flex;align-items:center;justify-content:center}

.hero{left:0;top:45px;width:1200px;height:643px;background:
  radial-gradient(ellipse 38% 22% at 72% 24%,rgba(246,248,252,.9),rgba(246,248,252,0) 70%),
  radial-gradient(ellipse 30% 16% at 35% 22%,rgba(230,236,242,.7),rgba(230,236,242,0) 70%),
  radial-gradient(ellipse 26% 55% at 2% 40%,rgba(34,70,32,.9),rgba(34,70,32,0) 72%),
  radial-gradient(ellipse 30% 45% at 100% 42%,rgba(92,140,44,.85),rgba(92,140,44,0) 72%),
  radial-gradient(ellipse 22% 20% at 14% 72%,rgba(128,62,26,.75),rgba(128,62,26,0) 72%),
  radial-gradient(ellipse 14% 14% at 42% 74%,rgba(140,78,34,.6),rgba(140,78,34,0) 72%),
  radial-gradient(ellipse 12% 14% at 88% 72%,rgba(40,30,24,.55),rgba(40,30,24,0) 72%),
  linear-gradient(180deg,#86b4e2 0%,#b9d0e4 16%,#c9d6dc 26%,#8fb070 40%,#6e9a3c 54%,#5c8c2c 74%,#44691f 100%)}
.brand-mark{left:106px;top:56px;width:150px;font-family:'Bebas Neue',sans-serif;font-size:23px;line-height:1.05;color:var(--green);text-align:center}
.nav{top:76px;font-size:13px;color:#2c2c2c}
.nav.active{font-weight:700;border-bottom:2px solid #2c2c2c;padding-bottom:2px}
.hero-welcome{top:162px;left:0;width:1200px;text-align:center;font-size:30px}
.hero-title{top:198px;left:0;width:1200px;text-align:center;font-size:80px;color:var(--green)}
.hero-sub{top:286px;left:330px;width:540px;text-align:center;font-size:19px;line-height:34px;color:#3a3a3a}
.hero-btn{left:523px;top:370px;width:150px;height:38px;background:var(--green);color:#fff;font-size:13px}

.about-title{left:111px;top:803px;font-size:48px}
.title-line{height:3px;background:var(--ink)}
.about-text{left:111px;top:868px;width:412px;font-size:15px;line-height:28.3px}
.about-btn{left:109px;top:1122px;width:172px;height:46px;background:var(--brown);color:#fff}
.photo{position:absolute}

.boxes{left:0;top:1297px;width:1200px;height:769px;background:
  radial-gradient(ellipse 30% 40% at 0% 50%,rgba(196,150,120,.35),rgba(196,150,120,0) 70%),
  radial-gradient(ellipse 30% 40% at 100% 40%,rgba(186,170,130,.35),rgba(186,170,130,0) 70%),
  var(--cream)}
.sec-title{left:0;width:1200px;text-align:center;font-size:48px}
.boxes-desc{left:200px;top:1444px;width:800px;text-align:center;font-size:14.5px;line-height:28px}
.box-card{position:absolute;top:1527px;width:309px;height:433px;background:var(--card);text-align:center}
.box-card .photo{left:36px;top:21px;width:237px;height:157px;border-radius:14px;border:4px solid #222;background:
  radial-gradient(ellipse 30% 40% at 30% 50%,rgba(236,200,205,.6),rgba(236,200,205,0) 70%),
  radial-gradient(ellipse 30% 40% at 72% 45%,rgba(236,200,205,.5),rgba(236,200,205,0) 70%),
  linear-gradient(135deg,#6e1824,#a84854 50%,#6e1824)}
.box-card .label{position:absolute;top:195px;width:100%;font-size:14px;color:#333}
.box-card .name{position:absolute;top:222px;width:100%;font-size:21px;font-weight:500;color:var(--ink)}
.box-card .desc{position:absolute;top:258px;left:30px;width:249px;font-size:13.5px;line-height:28px;color:#555}
.box-card .btn{left:80px;top:358px;width:145px;height:37px;background:var(--brown);color:#fff;font-size:13px}
.arrow{position:absolute;width:38px;height:38px}

.recipes{left:0;top:2066px;width:1200px;height:542px;background:linear-gradient(90deg,#1f1f1f,#2d2d2d 60%,#3a3a3a)}
.recipes-title{left:610px;top:2150px;font-size:48px;color:#fff}
.recipes-text{left:612px;top:2214px;width:412px;font-size:15px;line-height:28.3px;color:#fff;font-weight:500}
.recipes-btn{left:610px;top:2468px;width:172px;height:47px;background:var(--tan);color:var(--brown)}

.blog-card{position:absolute;top:2778px;width:307px;height:464px;background:#fff;box-shadow:0 2px 10px rgba(0,0,0,.12)}
.blog-card .photo{left:0;top:0;width:307px;height:212px}
.blog-card .date{position:absolute;left:22px;top:200px;height:30px;padding:0 12px;border-radius:15px;background:var(--green);color:#fff;font-size:13px;display:flex;align-items:center}
.blog-card .headline{position:absolute;left:19px;top:240px;font-size:20px;font-weight:500;color:var(--ink)}
.blog-card .rule{position:absolute;left:19px;width:270px;height:1px;background:#ddd}
.blog-card .excerpt{position:absolute;left:19px;top:291px;width:262px;font-size:14px;line-height:27.5px;color:#666}
.blog-card .avatar{position:absolute;left:8px;top:395px;width:52px;height:52px;border-radius:50%;background:linear-gradient(#cfd5dc,#9aa4ae)}
.blog-card .author{position:absolute;left:74px;top:412px;font-size:14px;color:#333}
.blog-card .go{position:absolute;left:240px;top:395px;width:52px;height:52px;border-radius:50%;background:var(--brown);display:flex;align-items:center;justify-content:center}

.footer{left:0;top:3418px;width:1200px;height:436px;background:var(--footer)}
.cta{left:111px;top:3333px;width:975px;height:169px;border-radius:85px;background:linear-gradient(90deg,#c9a878,#d9bd92 50%,#c7a474)}
.cta-text{left:173px;top:3400px;font-size:42px;color:#1a1a1a}
.cta-btn{left:884px;top:3396px;width:171px;height:46px;background:var(--brown);color:#fff}
.foot-brand{left:92px;top:3600px;width:210px;text-align:center;font-family:'Bebas Neue',sans-serif;font-size:36px;line-height:1.02;color:#fff}
.copy{left:80px;top:3774px;width:232px;text-align:center;font-size:13px;line-height:26px;color:#fff}
.news-label{left:392px;top:3576px;font-size:13px;font-weight:600;color:#fff}
.news-head{left:395px;top:3612px;font-size:22px;line-height:32px;font-weight:500;color:#fff}
.email{left:399px;top:3690px;width:254px;height:28px;border-bottom:1px solid #ccc;font-size:13px;color:#fff;display:flex;align-items:flex-start;gap:8px;padding-left:2px}
.sub-btn{left:401px;top:3752px;width:150px;height:40px;background:var(--tan);color:var(--brown);font-size:13px}
.foot-links{font-size:14px;line-height:27.7px;color:#fff}
</style>
</head>
<body>

<div class="abs topbar">FREE SHIPPING ON ALL ORDERS ACROSS US OVER $35!</div>

<!-- Hero -->
<div class="abs hero" role="img" aria-label="Brown and white cattle grazing in a green open-range valley beneath snow-capped mountains"></div>
<div class="abs brand-mark">LARKIN RIDGE<br>PROVISIONS CO</div>
<a class="abs nav active" style="left:340px">HOME</a>
<a class="abs nav" style="left:424px">ABOUT US</a>
<a class="abs nav" style="left:537px">MEAT BOXES</a>
<a class="abs nav" style="left:667px">RECIPES</a>
<a class="abs nav" style="left:767px">CONTACT US.</a>
<svg class="abs" style="left:1018px;top:73px" width="22" height="22" viewBox="0 0 22 22" fill="none" stroke="#222" stroke-width="2"><circle cx="9" cy="9" r="7"/><path d="M14 14l6 6"/></svg>
<svg class="abs" style="left:1056px;top:62px" width="34" height="34" viewBox="0 0 34 34" fill="none" stroke="#222" stroke-width="1.8"><path d="M2 12h4l3 12h13l3-9H8"/><circle cx="11" cy="28" r="1.6"/><circle cx="20" cy="28" r="1.6"/><circle cx="27" cy="8" r="6" fill="var(--green)" stroke="none"/><text x="27" y="11" font-size="9" fill="#fff" stroke="none" text-anchor="middle" font-family="Montserrat,sans-serif">0</text></svg>
<div class="abs display hero-welcome">WELCOME TO</div>
<div class="abs display hero-title">LARKIN RIDGE PROVISIONS CO</div>
<div class="abs hero-sub">Lorem Ipsum is simply dummy text of the printing and typesetting industry.</div>
<div class="btn hero-btn">GET STARTED</div>

<!-- About -->
<div class="abs display about-title">ABOUT US</div>
<div class="abs title-line" style="left:292px;top:826px;width:58px"></div>
<p class="abs about-text">Lorem Ipsum is simply dummy text of the printing and typesetting industry. Lorem Ipsum has been the industry's standard dummy text ever since the 1500s, when an unknown printer took a galley of type and scrambled it to make a type specimen book. It has survived not only five centuries, but also the leap into electronic typesetting, remaining essentially unchanged.</p>
<div class="btn about-btn">READ MORE</div>
<div class="photo" style="left:615px;top:787px;width:224px;height:141px;background:radial-gradient(ellipse 45% 45% at 55% 50%,#c23a3e,rgba(194,58,62,0) 75%),linear-gradient(180deg,#2a2a2a,#4a3426 60%,#6a4a30)" role="img" aria-label="Raw steak with rosemary on a wooden board"></div>
<div class="photo" style="left:615px;top:941px;width:224px;height:254px;background:linear-gradient(170deg,#eae6e2 0%,#dcd6d2 40%,#d6606a 62%,#c23b46 100%)" role="img" aria-label="Chef slicing raw beef with a knife"></div>
<div class="photo" style="left:854px;top:838px;width:225px;height:317px;background:radial-gradient(ellipse 50% 35% at 50% 45%,#6b3a22,rgba(107,58,34,0) 75%),radial-gradient(ellipse 40% 20% at 45% 80%,#a8484a,rgba(168,72,74,0) 75%),linear-gradient(180deg,#2e2e2e,#1e1e1e)" role="img" aria-label="Grilled steak sliced on a dark plate with herbs"></div>

<!-- Meat boxes -->
<div class="abs boxes" role="img" aria-label="Faded background of raw beef cuts and herbs"></div>
<div class="abs title-line" style="left:418px;top:1398px;width:60px"></div>
<div class="abs display sec-title" style="top:1376px">MEAT BOXES</div>
<div class="abs title-line" style="left:721px;top:1398px;width:60px"></div>
<p class="abs boxes-desc">Lorem Ipsum is simply dummy text of the printing and typesetting industry. Lorem Ipsum has been the industry's standard dummy text ever since the 1500s,</p>

<div class="box-card" style="left:109px">
  <div class="photo" role="img" aria-label="Marbled ribeye steaks in a black tray"></div>
  <div class="label">Lorem Ipsum</div><div class="name">Lorem Ipsum</div>
  <div class="desc">Lorem Ipsum is simply dummy text of the printing and typesetting industry.</div>
  <div class="btn">ADD TO CART</div>
</div>
<div class="box-card" style="left:443px">
  <div class="photo" role="img" aria-label="Marbled ribeye steaks in a black tray"></div>
  <div class="label">Lorem Ipsum</div><div class="name">Lorem Ipsum</div>
  <div class="desc">Lorem Ipsum is simply dummy text of the printing and typesetting industry.</div>
  <div class="btn">ADD TO CART</div>
</div>
<div class="box-card" style="left:778px">
  <div class="photo" role="img" aria-label="Marbled ribeye steaks in a black tray"></div>
  <div class="label">Lorem Ipsum</div><div class="name">Lorem Ipsum</div>
  <div class="desc">Lorem Ipsum is simply dummy text of the printing and typesetting industry.</div>
  <div class="btn">ADD TO CART</div>
</div>
<svg class="arrow" style="left:33px;top:1739px" viewBox="0 0 38 38" fill="none" stroke="#777" stroke-width="2"><circle cx="19" cy="19" r="17"/><path d="M22 11l-8 8 8 8"/></svg>
<svg class="arrow" style="left:1123px;top:1739px" viewBox="0 0 38 38" fill="none" stroke="#111" stroke-width="2.4"><circle cx="19" cy="19" r="17"/><path d="M16 11l8 8-8 8"/></svg>

<!-- Recipes -->
<div class="abs recipes"></div>
<div class="photo" style="left:0;top:2066px;width:600px;height:542px;background:radial-gradient(ellipse 28% 26% at 30% 42%,#b02a32,rgba(176,42,50,0) 75%),radial-gradient(ellipse 24% 22% at 12% 85%,#9a2028,rgba(154,32,40,0) 75%),radial-gradient(ellipse 22% 20% at 65% 8%,#a0242c,rgba(160,36,44,0) 75%),radial-gradient(ellipse 20% 22% at 4% 18%,#8a1c24,rgba(138,28,36,0) 75%),linear-gradient(90deg,#2a2626,#232323)" role="img" aria-label="Raw beef fillets with peppercorns and rosemary on dark stone"></div>
<div class="abs display recipes-title">OUR RECIPES</div>
<div class="abs" style="left:848px;top:2174px;width:58px;height:3px;background:#fff"></div>
<p class="abs recipes-text">Lorem Ipsum is simply dummy text of the printing and typesetting industry. Lorem Ipsum has been the industry's standard dummy text ever since the 1500s, when an unknown printer took a galley of type and scrambled it to make a type specimen book. It has survived not only five centuries, but also the leap into electronic typesetting, remaining essentially unchanged.</p>
<div class="btn recipes-btn">READ MORE</div>

<!-- Blog -->
<div class="abs title-line" style="left:427px;top:2725px;width:60px"></div>
<div class="abs display sec-title" style="top:2703px">OUR BLOG</div>
<div class="abs title-line" style="left:712px;top:2725px;width:60px"></div>

<div class="blog-card" style="left:106px">
  <div class="photo" style="background:radial-gradient(ellipse 30% 35% at 35% 50%,#b8282e,rgba(184,40,46,0) 75%),radial-gradient(ellipse 25% 30% at 75% 70%,#c0302e,rgba(192,48,46,0) 75%),linear-gradient(135deg,#3e3e3e,#2a2a2a)" role="img" aria-label="Raw steaks with rosemary and salt on slate"></div>
  <div class="date">February 11, 2024</div>
  <div class="headline">Lorem Ipsum is simply</div>
  <div class="rule" style="top:275px"></div>
  <div class="excerpt">Lorem Ipsum is simply dummy text of the printing and typesetting industry. Lorem Ipsum</div>
  <div class="rule" style="top:382px"></div>
  <div class="avatar" role="img" aria-label="Author portrait"></div>
  <div class="author">Dorian Pell</div>
  <div class="go"><svg width="20" height="20" viewBox="0 0 20 20" fill="none" stroke="#fff" stroke-width="2.4"><path d="M4 16L16 4M7 4h9v9"/></svg></div>
</div>
<div class="blog-card" style="left:446px">
  <div class="photo" style="background:radial-gradient(ellipse 35% 35% at 40% 55%,#e0909a,rgba(224,144,154,0) 75%),radial-gradient(ellipse 25% 30% at 85% 30%,#5e7a34,rgba(94,122,52,0) 75%),linear-gradient(135deg,#8a5a3a,#b86e6e 55%,#6a4a30)" role="img" aria-label="Assorted raw meat cuts with herbs on a board"></div>
  <div class="date">February 11, 2024</div>
  <div class="headline">Lorem Ipsum is simply</div>
  <div class="rule" style="top:275px"></div>
  <div class="excerpt">Lorem Ipsum is simply dummy text of the printing and typesetting industry. Lorem Ipsum</div>
  <div class="rule" style="top:382px"></div>
  <div class="avatar" role="img" aria-label="Author portrait"></div>
  <div class="author">Dorian Pell</div>
  <div class="go"><svg width="20" height="20" viewBox="0 0 20 20" fill="none" stroke="#fff" stroke-width="2.4"><path d="M4 16L16 4M7 4h9v9"/></svg></div>
</div>
<div class="blog-card" style="left:781px">
  <div class="photo" style="background:radial-gradient(ellipse 25% 18% at 40% 75%,#7a2a24,rgba(122,42,36,0) 75%),linear-gradient(180deg,#1c1c1c,#222 60%,#141414)" role="img" aria-label="Chef seasoning a steak in a dark kitchen"></div>
  <div class="date">February 11, 2024</div>
  <div class="headline">Lorem Ipsum is simply</div>
  <div class="rule" style="top:275px"></div>
  <div class="excerpt">Lorem Ipsum is simply dummy text of the printing and typesetting industry. Lorem Ipsum</div>
  <div class="rule" style="top:382px"></div>
  <div class="avatar" role="img" aria-label="Author portrait"></div>
  <div class="author">Dorian Pell</div>
  <div class="go"><svg width="20" height="20" viewBox="0 0 20 20" fill="none" stroke="#fff" stroke-width="2.4"><path d="M4 16L16 4M7 4h9v9"/></svg></div>
</div>
<svg class="arrow" style="left:33px;top:3006px" viewBox="0 0 38 38" fill="none" stroke="#777" stroke-width="2"><circle cx="19" cy="19" r="17"/><path d="M22 11l-8 8 8 8"/></svg>
<svg class="arrow" style="left:1122px;top:3006px" viewBox="0 0 38 38" fill="none" stroke="#111" stroke-width="2.4"><circle cx="19" cy="19" r="17"/><path d="M16 11l8 8-8 8"/></svg>

<!-- Footer -->
<div class="abs footer"></div>
<div class="abs cta"></div>
<div class="abs display cta-text">CONTACT US FOR DOOR STEP DELIVERY</div>
<div class="btn cta-btn">CONTACT US</div>

<div class="abs foot-brand">LARKIN RIDGE<br>PROVISIONS CO</div>
<p class="abs copy">© 2024 Larkin Ridge Provisions Co |<br>All Rights Reserved</p>

<div class="abs news-label">Our Newsletter</div>
<div class="abs news-head">Stay Up To Date with<br>Larkin Ridge</div>
<div class="abs email"><svg width="16" height="14" viewBox="0 0 16 14" fill="none" stroke="#fff" stroke-width="1.2" style="margin-top:3px"><rect x="1" y="2" width="14" height="10"/><path d="M1 2l7 6 7-6"/></svg>Enter Your Email</div>
<div class="btn sub-btn">SUBSCRIBE</div>

<div class="abs foot-links" style="left:754px;top:3570px">Home<br>About Us,<br>Meat Boxes<br>Recipes<br>Contact Us.</div>
<div class="abs foot-links" style="left:929px;top:3570px">Privacy Policy<br>Careers<br>Terms Condition</div>

</body>
</html>
```